Patient Report Folder for modern Chiropractic Clinic

We are looking for someone to design a patient folder and 3 simple info sheets to go along with it.

The design should be clean and masculine with an artsy touch. I am a fan of the Fra Mollego style drawings so would like the background to be a style of parchment paper. The info sheets should follow a similar style.

Please check the “Design Outline” pdf and the “Folder Design” file before getting started. The 3 info sheets are going to be placed in the pocket where “Attachment #3” will be.

- The format should be DIN A4 according to the printing details attached in the files section. Please see the ''Folder Design.jpg'' for the design of the folder.
- All the designs should be different and unique in nature but match each other.
- The text for Info Sheet #3 can be left blank.

It is probably best to take a look at the ''Design Outline'' file first to see how I envision the design to be. Please do not hesitate to ask me questions or to discuss ideas.

Target Market(s)

upper class audience with a focus on health and well-being

Industry/Entity Type

Chiropractic // Health

Requirements
Must have
• The colours should be fitting with the main colours in the logo: #1ccad5 and #b1b2b4
Nice to have
• Fra Mollego Style design and the background on parchment paper style. It is not a must but if anyone can come up with a suitable design and colorway that would be great.

```html
<!DOCTYPE html>
<html lang="en">
<head>
<meta charset="utf-8">
<title>Nordlicht Patient Folder</title>
<link href="https://fonts.googleapis.com/css2?family=Poppins:wght@400;500;600&display=swap" rel="stylesheet">
<style>
  :root {
    --stage-dark: #2c2c2c;
    --stage-mid: #373737;
    --folder-bronze: #a6813f;
    --folder-sand: #d1a96b;
    --ink-dark: #1a1408;
    --ink-brown: #7a5522;
    --cut-line: #2fa043;
    --fold-mark: #555555;
    --label-white: #ffffff;
  }
  html, body {
    margin: 0;
    padding: 0;
    width: 1200px;
    height: 1200px;
    overflow: hidden;
  }
  body {
    background: linear-gradient(90deg, var(--stage-dark) 0%, var(--stage-mid) 55%, var(--stage-dark) 100%);
    font-family: "Poppins", sans-serif;
  }
  .folder-dieline {
    display: block;
    width: 1200px;
    height: 1200px;
  }
  .quote-text {
    font-family: "Poppins", sans-serif;
    font-size: 20px;
    font-weight: 400;
    letter-spacing: 2.6px;
    fill: var(--ink-dark);
  }
  .quote-author {
    letter-spacing: 5px;
  }
  .contact-text {
    font-family: "Poppins", sans-serif;
    font-size: 17px;
    font-weight: 400;
    fill: var(--ink-dark);
  }
  .contact-web {
    font-weight: 500;
  }
  .flap-slogan {
    font-family: "Poppins", sans-serif;
    font-size: 17px;
    font-weight: 600;
    letter-spacing: 4px;
    fill: var(--ink-dark);
  }
  .brand-name {
    font-family: "Poppins", sans-serif;
    font-size: 62px;
    font-weight: 500;
    letter-spacing: 2px;
    fill: var(--ink-brown);
  }
  .patient-label {
    font-family: "Poppins", sans-serif;
    font-size: 18px;
    font-weight: 600;
    letter-spacing: 5px;
    fill: var(--ink-brown);
  }
</style>
</head>
<body>
<svg class="folder-dieline" viewBox="0 0 1932 1932" xmlns="http://www.w3.org/2000/svg">
  <defs>
    <clipPath id="front-panel-area">
      <rect x="143" y="64" width="1744" height="1221"/>
    </clipPath>
  </defs>

  <path class="folder-shape" fill="var(--folder-bronze)"
        d="M143,64 H1887 V1285 H993 V1450 C996,1520 980,1545 925,1565 L143,1866 V1285 H123 L44,1250 V744 L123,722 H143 Z"/>

  <g class="front-cover" clip-path="url(#front-panel-area)" fill="var(--folder-sand)">
    <circle cx="1040" cy="675" r="597"/>
    <rect x="993" y="64" width="894" height="1221"/>
  </g>

  <path class="cut-line" fill="none" stroke="var(--cut-line)" stroke-width="1.5"
        d="M143,64 H1887 V1285 H993 V1450 C996,1520 980,1545 925,1565 L143,1866 V1285 H123 L44,1250 V744 L123,722 H143 Z"/>

  <g class="fold-marks" stroke="var(--fold-mark)" stroke-width="2">
    <line x1="1004" y1="606" x2="1004" y2="711"/>
    <line x1="1028" y1="606" x2="1028" y2="711"/>
    <line x1="517" y1="634" x2="525" y2="634"/>
    <line x1="641" y1="634" x2="649" y2="634"/>
  </g>

  <text class="quote-text" x="203" y="138">THE GREATEST WEALTH IS HEALTH</text>
  <text class="quote-text quote-author" x="203" y="166">- AUREL BRENN</text>

  <g class="contact-block">
    <line x1="204" y1="1141" x2="204" y2="1226" stroke="var(--ink-brown)" stroke-width="2"/>
    <g class="icon-pin" fill="none" stroke="var(--ink-brown)" stroke-width="1.6">
      <path d="M240,1155 C235,1149 235,1147 235,1146 A5,5 0 1 1 245,1146 C245,1147 245,1149 240,1155 Z"/>
      <circle cx="240" cy="1146" r="1.6"/>
    </g>
    <g class="icon-mail" fill="none" stroke="var(--ink-brown)" stroke-width="1.6">
      <rect x="234.5" y="1186" width="11" height="9" rx="1.5"/>
      <path d="M234.5,1187 L240,1191.5 L245.5,1187"/>
    </g>
    <g class="icon-web" fill="none" stroke="var(--ink-brown)" stroke-width="1.4">
      <circle cx="240" cy="1218" r="5.5"/>
      <line x1="234.5" y1="1218" x2="245.5" y2="1218"/>
      <ellipse cx="240" cy="1218" rx="2.3" ry="5.5"/>
    </g>
    <text class="contact-text" x="255" y="1155">Lindenhofweg 12,</text>
    <text class="contact-text" x="255" y="1173">70469 Stuttgart-Feuerbach</text>
    <text class="contact-text" x="255" y="1197">info@praxisnordlicht.de</text>
    <text class="contact-text contact-web" x="255" y="1223">praxisnordlicht.de</text>
  </g>

  <text class="flap-slogan" transform="rotate(180 446 1358)" x="446" y="1364" text-anchor="middle">LEAVE YOUR WORRIES BEHIND...</text>

  <g class="brand-block">
    <circle cx="1446" cy="630" r="114" fill="none" stroke="var(--ink-brown)" stroke-width="5"/>
    <text class="brand-name" x="1458" y="830" text-anchor="middle">NORDLICHT</text>
  </g>

  <text class="patient-label" x="1457" y="1139" text-anchor="middle">PATIENT'S NAME</text>
  <rect class="patient-field" x="1247" y="1155" width="420" height="48" fill="var(--label-white)"/>
</svg>
</body>
</html>
```